Nine Lanterns Quill House Book Cover for: "Growing Older Wisely"

We are a publishing company who plans to launch the book, Growing Older Wisely, A Handy Compact Manual for Legal, Financial and Emotional Health in late 2018. We desire a book cover that creates interest, looks professional and can draw readers to open and purchase this book. Growing Older Wisely is an invaluable, self-help book which provides Generation X, Baby Boomers and their families with the following information: steps to obtain valid, reliable wills and trusts, identify and pay for health care, address end of life care and manage grief. (Please see the attached book description for more information about the book contents). The cover needs to have a "wellness", health and healing emphasis but it should not be morbid. Instead, the cover should have an uplifting, inviting and engaging feeling.

The designer should use Photoshop to develop the 5 x 7 cover. Please design the front, back cover and spine using the attached suggested layout as a guide. Use colors that complement the background colors in the author's photo and the logo for the front and back colors. Feel free to change the colors of the black rectangles on the front of the book. We are looking for a design to be added using the suggested layouts but we are open to modifications of the layout provided that all the content in the attachments are used. Below are the specifications needed for the cover:

-Use Photoshop
-Develop a front and back cover for a 5 x 7 format book
-Include the book title, subtitle and author name on the front cover as noted on the front cover attachment
-Include a book title and author names on the spine of the cover
-Use full bleed background if appropriate
-Color correct and resize images as necessary
-Insert logo and publisher’s imprint on spine and back cover as noted in attachments

For designers who are successful with this contest, we will primarily consider you for future projects.

Thanks!

Target Market(s)

Generation X, Baby Boomers and their families

Industry/Entity Type

Book Publisher

Font styles to use
Sans Serif

Colors

Designer to choose colors to be used in the design.

Requirements
Must have
• The designer should use Photoshop to develop the 5 x 7 cover. Please design the front, back cover and spine using the attached suggested layout as a guide. Use colors that complement the background colors in the author's photo and the logo for the front and back colors. Feel free to change the colors of the black rectangles on the front of the book. We are looking for a design to be added using the suggested layouts but we are open to modifications of the layout provided that all the content in the attachments are used. Below are the specifications needed for the cover:
• -Use Photoshop
• -Develop a front and back cover for a 5 x 7 format book
• -Include the book title, subtitle and author name on the front cover as noted on the front cover attachment
• -Include a book title and author names on the spine of the cover
• -Use full bleed background if appropriate
• -Color correct and resize images as necessary
• -Insert logo and publisher’s imprint on spine and back cover as noted in attachments
Nice to have
• N/A
Should not have
• The design should not specifically duplicate the layout samples or include pictures of persons on the cover. We have provided those as a guide; we are looking for innovation and professionalism.

```html
<!DOCTYPE html>
<html lang="en">
<head>
<meta charset="utf-8">
<title>Growing Older Wisely — Front Cover</title>
<link rel="stylesheet" href="https://fonts.googleapis.com/css2?family=Cinzel:wght@400;500&family=Cormorant+Garamond:ital,wght@1,500&display=swap">
<style>
  :root {
    --page-bg: #e8e5df;
    --cover-bg: #ffffff;
    --ink-brown: #4a3512;
    --soil-brown: #4b360f;
    --author-cream: #efe6c6;
    --accent-red: #e3101b;
    --ink-dark: #1c160c;
    --bulb-yellow: #f3ea1a;
    --leaf-green: #cfe2b4;
  }
  * { margin: 0; padding: 0; box-sizing: border-box; }
  html, body {
    width: 1200px;
    height: 1200px;
    overflow: hidden;
    background: var(--page-bg);
  }
  .cover {
    position: absolute;
    left: 220px;
    top: 40px;
    width: 760px;
    height: 1120px;
    background: var(--cover-bg);
    overflow: hidden;
  }
  .endorsement {
    position: absolute;
    top: 42px;
    left: 0;
    width: 100%;
    text-align: center;
    color: var(--ink-dark);
  }
  .endorsement-quote {
    font-family: "Cormorant Garamond", serif;
    font-style: italic;
    font-weight: 500;
    font-size: 30px;
    letter-spacing: 4px;
    line-height: 34px;
    padding-left: 20px;
  }
  .endorsement-source {
    font-family: "Cinzel", serif;
    font-size: 26px;
    letter-spacing: 4px;
    line-height: 34px;
    padding-left: 20px;
  }
  .title {
    position: absolute;
    top: 131px;
    left: 0;
    width: 100%;
    text-align: center;
    font-family: "Cinzel", serif;
    font-weight: 400;
    font-size: 80px;
    line-height: 96px;
    color: var(--ink-brown);
    padding-left: 20px;
  }
  .title span { display: block; }
  .cover-illustration {
    position: absolute;
    left: 252px;
    top: 437px;
    width: 271px;
    height: 330px;
    border-radius: 24px;
    background:
      radial-gradient(ellipse 55% 50% at 50% 42%, var(--bulb-yellow) 0%, #f6ef6a 55%, var(--leaf-green) 85%, #f3f6ee 100%);
  }
  .subtitle {
    position: absolute;
    left: 390px;
    top: 778px;
    white-space: nowrap;
    font-family: "Cinzel", serif;
    font-size: 19px;
    line-height: 27px;
    color: var(--ink-dark);
    text-transform: uppercase;
  }
  .subtitle .highlight { color: var(--accent-red); }
  .soil-band {
    position: absolute;
    left: 0;
    bottom: 0;
    width: 100%;
    height: 174px;
    background: var(--soil-brown);
  }
  .authors {
    position: absolute;
    left: 0;
    top: 48px;
    width: 100%;
    text-align center;
    text-align: center;
    padding-left: 50px;
    font-family: "Cinzel", serif;
    color: var(--author-cream);
    text-transform: uppercase;
  }
  .author-primary {
    font-size: 38px;
    line-height: 44px;
    letter-spacing: 1px;
  }
  .author-secondary {
    font-size: 29px;
    line-height: 38px;
    letter-spacing: 1px;
  }
</style>
</head>
<body>
  <main class="cover">
    <header class="endorsement">
      <p class="endorsement-quote">“INDISPENSABLE!”</p>
      <p class="endorsement-source">--THE RIVERBEND LEDGER</p>
    </header>

    <h1 class="title">
      <span>GROWING</span>
      <span>OLDER</span>
      <span>WISELY</span>
    </h1>

    <div class="cover-illustration" role="img" aria-label="Illustration of a glowing yellow light bulb growing like a young tree from the soil, with leafy branches and two small birds perched on it"></div>

    <p class="subtitle">
      A Handy Compact Manual for<br>
      <span class="highlight">Legal</span>, <span class="highlight">Financial</span> and<br>
      <span class="highlight">Emotional Health</span>
    </p>

    <footer class="soil-band">
      <div class="authors">
        <p class="author-primary">Maren T. Holloway, M.P.A.</p>
        <p class="author-secondary">with Dale R. Whitcomb, Esq.</p>
      </div>
    </footer>
  </main>
</body>
</html>
```